Premium stylish simple clever card design for high end construction company.

I need a business card designed that is a standard size and shape (square edges) that is black in colour, with black edges. All text is to be either grey/silver or yellow/gold. On the front I want the logo (supplied as attachment g5) to be embossed or raised to give a texture. I also want the name of my company "The Kestrel Vault (larger font) construction co. (smaller font)" I like the clean style (found in attachment 56419286) of the black background with silver text. But the triangle is to be gold/yellow.

On the back needs to have my contact details. In silver or gold text.

Liam Porter - Builder
Liam@thekestrelvault.com.au
www.thekestrelvault.com.au
0427391065
Lic 517904k
PO BOX 739 Wrenfield NSW 2107

Must look simple, elegant and precise.

My work is of the utmost quality and my business card needs to project that. It needs to be simple and precise. It should scream luxury and confidence. Feel free to get creative with the font and font size. If you google "The Kestrel Vault" you will see it has links to great architecture, art, nature and the fibonacci sequence so i am open to using these ideas also.

Target Market(s)

High End home owners. 30-70 year olds.

Industry/Entity Type

Residential Construction

Contact Information for Business Card

Logo and company name on front. Contact details on back.

Font styles to use
Serif
Sans Serif

Colors
ffcf3e

Requirements
Must have
• black background
Nice to have
• debossed logo (silver and gold)
• debased company name (silver)
Should not have
• It should not look like a standard construction business card with pictures of hammers or tools etc.

```html
<!DOCTYPE html>
<html lang="en">
<head>
<meta charset="utf-8">
<title>The Kestrel Vault – Business Card</title>
<link rel="stylesheet" href="https://fonts.googleapis.com/css2?family=Source+Sans+3:wght@300;400;600&display=swap">
<style>
  :root {
    --backdrop: #8a6a45;
    --card-black: #0c0c0d;
    --card-sheen: #1e1e20;
    --gold: #ffcf3e;
    --gold-soft: #e2b93a;
    --silver: #c9c9cb;
    --silver-dim: #9a9a9c;
  }
  * { margin: 0; padding: 0; box-sizing: border-box; }
  html, body { width: 1200px; height: 1023px; overflow: hidden; }
  body {
    background: var(--backdrop);
    font-family: "Source Sans 3", "Myriad Pro", sans-serif;
    position: relative;
  }
  .card {
    position: absolute;
    width: 580px;
    height: 332px;
    background: linear-gradient(135deg, var(--card-sheen) 0%, var(--card-black) 45%, var(--card-black) 100%);
    box-shadow: 0 18px 40px rgba(0,0,0,0.45);
  }
  .card--contact { left: 70px; top: 110px; }
  .card--brand { left: 550px; top: 580px; }

  /* Contact side */
  .contact__mark {
    position: absolute;
    right: 28px; top: 28px;
    display: flex; align-items: center; gap: 10px;
    color: var(--silver);
    font-size: 15px; font-weight: 400; letter-spacing: 0.04em;
  }
  .contact__mark-dot {
    width: 56px; height: 56px; border-radius: 50%;
    border: 7px solid var(--silver);
    flex: none;
  }
  .contact__name {
    position: absolute;
    right: 232px; top: 34px;
    color: var(--gold);
    font-size: 34px; font-weight: 400;
    line-height: 1;
    white-space: nowrap;
  }
  .contact__rule {
    position: absolute;
    left: 30px; right: 232px; top: 80px;
    height: 1.5px; background: var(--gold-soft);
  }
  .contact__role {
    position: absolute;
    right: 232px; top: 86px;
    color: var(--silver);
    font-size: 19px; font-weight: 400;
  }
  .contact__address {
    position: absolute;
    left: 30px; top: 150px;
    color: var(--gold);
    font-size: 19px; font-weight: 400;
    white-space: nowrap;
  }
  .contact__list {
    position: absolute;
    left: 30px; top: 192px;
    list-style: none;
    color: var(--silver);
    font-size: 16px; line-height: 24px;
  }
  .contact__list li { display: flex; align-items: center; gap: 10px; white-space: nowrap; }
  .contact__icon { width: 14px; height: 14px; flex: none; }
  .contact__icon--blank { width: 14px; }

  /* Brand side */
  .brand__rule {
    position: absolute;
    height: 1.5px; background: var(--silver-dim);
  }
  .brand__rule--top { left: 50px; width: 200px; top: 80px; }
  .brand__rule--bottom { right: 40px; width: 200px; top: 176px; }
  .brand {
    position: absolute;
    left: 50px; top: 92px;
  }
  .brand__name {
    color: var(--silver);
    font-size: 42px; font-weight: 300;
    letter-spacing: 0.05em; text-transform: uppercase;
    line-height: 1;
    white-space: nowrap;
  }
  .brand__sub {
    margin-left: 150px;
    margin-top: 4px;
    color: var(--silver-dim);
    font-size: 12px; font-weight: 300;
    letter-spacing: 0.2em; text-transform: uppercase;
  }
  .brand__dot {
    position: absolute;
    right: 40px; top: 28px;
    width: 60px; height: 60px; border-radius: 50%;
    border: 8px solid var(--silver);
  }
  .brand__tagline {
    position: absolute;
    left: 50px; top: 200px;
    color: var(--gold);
    font-size: 24px; font-weight: 400;
    white-space: nowrap;
  }
</style>
</head>
<body>

  <section class="card card--contact" aria-label="Contact side">
    <div class="contact__mark"><span class="contact__mark-dot"></span>The Kestrel Vault</div>
    <h1 class="contact__name">Liam Porter</h1>
    <div class="contact__rule"></div>
    <p class="contact__role">Builder</p>
    <p class="contact__address">PO BOX 739 Wrenfield NSW 2107</p>
    <ul class="contact__list">
      <li>
        <svg class="contact__icon" viewBox="0 0 14 14"><rect x="1" y="3" width="12" height="8" fill="#e2b93a"/><path d="M1 3 L7 8 L13 3" fill="none" stroke="#0c0c0d" stroke-width="1"/></svg>
        Liam@thekestrelvault.com.au
      </li>
      <li>
        <svg class="contact__icon" viewBox="0 0 14 14"><circle cx="7" cy="7" r="6" fill="#e2b93a"/><path d="M1 7 H13 M7 1 V13" stroke="#0c0c0d" stroke-width="0.8"/><ellipse cx="7" cy="7" rx="3" ry="6" fill="none" stroke="#0c0c0d" stroke-width="0.8"/></svg>
        www.thekestrelvault.com.au
      </li>
      <li>
        <svg class="contact__icon" viewBox="0 0 14 14"><path d="M3 1 L5.5 1 L6 4.5 L4.5 5.5 C5.3 7.5 6.5 8.7 8.5 9.5 L9.5 8 L13 8.5 L13 11 C13 12 12 13 11 13 C5.5 12.5 1.5 8.5 1 3 C1 2 2 1 3 1 Z" fill="#e2b93a"/></svg>
        0427391065
      </li>
      <li><span class="contact__icon contact__icon--blank"></span>Lic 517904k</li>
    </ul>
  </section>

  <section class="card card--brand" aria-label="Brand side">
    <span class="brand__dot"></span>
    <div class="brand__rule brand__rule--top"></div>
    <div class="brand">
      <h2 class="brand__name">The Kestrel Vault</h2>
      <p class="brand__sub">Construction co.</p>
    </div>
    <div class="brand__rule brand__rule--bottom"></div>
    <p class="brand__tagline">The Kestrel Vault construction co.</p>
  </section>

</body>
</html>
```